Business Card Design needed for logo design project

This project is linked to a href='http://jobs.pixelfennel.example/job.aspx?id=412907'Tide Nook: Design a logo for our new trailer boat syndication business in Sydney
Our company needs a Business Card Design. Please refer to our original project in the link above.
I would like a relatively simple and classy business card design. could you please also use small symbols for identifying contact info eg. mobile, web and email?
Updates
Please see my new project to design a business card for a trailer boat syndication business in Sydney, Australia.
Industry/Entity Type
Business
Look and feel
Each slider illustrates characteristics of the customer's brand and the style your logo design should communicate.

```html
<!DOCTYPE html>
<html lang="en">
<head>
<meta charset="utf-8">
<title>Tide Nook – Business Card</title>
<link rel="stylesheet" href="https://fonts.googleapis.com/css2?family=Exo+2:wght@600;700&family=Michroma&display=swap">
<style>
  :root {
    --bg: #e9e6e1;
    --teal: #3fc3cc;
    --teal-deep: #2aa6b0;
    --ink: #3a3a3c;
    --ink-soft: #6b6b6e;
    --paper: #ffffff;
    --black: #101112;
    --black-soft: #2a2b2d;
  }
  * { box-sizing: border-box; margin: 0; padding: 0; }
  html, body { width: 1200px; height: 1023px; overflow: hidden; }
  body { background: var(--bg); position: relative; font-family: "Exo 2", sans-serif; }

  .card {
    position: absolute;
    width: 560px; height: 320px;
    border-radius: 4px;
    overflow: hidden;
    box-shadow: 0 10px 28px rgba(0,0,0,.18);
  }
  .card--front { left: 70px; top: 120px; background: var(--paper); }
  .card--back { left: 570px; top: 580px; background: linear-gradient(135deg, var(--black-soft), var(--black) 60%); }

  .card__shape { position: absolute; inset: 0; width: 100%; height: 100%; }

  .brand { position: absolute; left: 34px; top: 40px; }
  .brand__row { display: flex; align-items: center; gap: 10px; }
  .brand__dot { width: 14px; height: 14px; border-radius: 50%; background: var(--teal); }
  .brand__name { font-weight: 700; font-size: 40px; color: var(--teal); line-height: 1; }
  .brand__tagline {
    font-family: "Michroma", sans-serif; font-size: 6.5px; letter-spacing: .2px;
    color: var(--ink-soft); text-transform: uppercase; margin-top: 7px; margin-left: 24px;
    white-space: nowrap;
  }

  .person { position: absolute; left: 34px; top: 170px; display: flex; align-items: baseline; gap: 10px; }
  .person__name { font-weight: 700; font-size: 26px; color: var(--ink); }
  .person__sep { font-size: 22px; color: var(--ink); }
  .person__role { font-weight: 700; font-size: 13px; color: var(--ink); }

  .contacts { position: absolute; left: 34px; top: 218px; list-style: none; }
  .contacts__item {
    display: flex; align-items: center; gap: 10px; margin-bottom: 7px;
    font-family: "Michroma", sans-serif; font-size: 10px; letter-spacing: 1.5px; color: var(--ink);
  }
  .contacts__icon { width: 14px; height: 14px; border-radius: 2px; background: var(--teal); flex: none; }

  .address {
    position: absolute; right: 24px; top: 34px; text-align: right; font-style: normal;
    font-family: "Michroma", sans-serif; font-size: 9px; letter-spacing: 1px; color: var(--ink); line-height: 2;
    white-space: nowrap;
  }
  .address__company { font-family: "Exo 2", sans-serif; font-weight: 700; font-size: 13px; letter-spacing: 1px; }

  .back-brand { position: absolute; left: 0; right: 0; top: 118px; text-align: center; }
  .back-brand__row { display: inline-flex; align-items: center; gap: 12px; }
  .back-brand__name { font-weight: 700; font-size: 50px; color: var(--teal); line-height: 1; }
  .back-brand__dot { width: 16px; height: 16px; border-radius: 50%; background: var(--teal); }
  .back-brand__tagline {
    font-family: "Michroma", sans-serif; font-size: 8px; letter-spacing: .6px;
    color: var(--paper); text-transform: uppercase; margin-top: 10px;
  }
</style>
</head>
<body>

<section class="card card--front" aria-label="Business card front">
  <svg class="card__shape" viewBox="0 0 560 320" preserveAspectRatio="none" aria-hidden="true">
    <path d="M340 0 H560 V320 H330 C365 240 385 120 340 0 Z" fill="var(--teal)"/>
    <path d="M300 320 C420 260 470 170 470 0 H560 V320 Z" fill="var(--teal-deep)" opacity=".35"/>
    <path d="M332 0 C382 120 362 240 318 320 H300 C348 240 366 120 318 0 Z" fill="var(--black-soft)" opacity=".85"/>
    <path d="M380 320 C470 250 500 190 505 140 C475 210 430 265 380 320 Z" fill="var(--paper)"/>
  </svg>

  <div class="brand">
    <div class="brand__row">
      <span class="brand__dot"></span>
      <span class="brand__name">Tide Nook</span>
    </div>
    <p class="brand__tagline">Trailer boat syndication and management</p>
  </div>

  <div class="person">
    <span class="person__name">Dean Harlow</span>
    <span class="person__sep">|</span>
    <span class="person__role">Director</span>
  </div>

  <ul class="contacts">
    <li class="contacts__item">
      <svg class="contacts__icon" viewBox="0 0 14 14" aria-label="Phone"><rect width="14" height="14" rx="2" fill="var(--teal)"/><path d="M4 3.5 L5.5 3 L6.5 5 L5.6 5.8 C6.1 7 7 7.9 8.2 8.4 L9 7.5 L11 8.5 L10.5 10 C7 10 4 7 4 3.5 Z" fill="#fff"/></svg>
      555-014-0000
    </li>
    <li class="contacts__item">
      <svg class="contacts__icon" viewBox="0 0 14 14" aria-label="Email"><rect width="14" height="14" rx="2" fill="var(--teal)"/><rect x="3" y="4.5" width="8" height="5.5" fill="none" stroke="#fff" stroke-width="1"/><path d="M3 4.5 L7 7.5 L11 4.5" fill="none" stroke="#fff" stroke-width="1"/></svg>
      info@tidenook.com
    </li>
    <li class="contacts__item">
      <svg class="contacts__icon" viewBox="0 0 14 14" aria-label="Website"><rect width="14" height="14" rx="2" fill="var(--teal)"/><circle cx="7" cy="7" r="3.8" fill="none" stroke="#fff" stroke-width="1"/><path d="M3.2 7 H10.8 M7 3.2 C5.5 5 5.5 9 7 10.8 M7 3.2 C8.5 5 8.5 9 7 10.8" fill="none" stroke="#fff" stroke-width=".8"/></svg>
      www.tidenook.com
    </li>
  </ul>

  <address class="address">
    <span class="address__company">Tide Nook</span><br>
    P.O. Box 412<br>
    Fernby, OH 43999
  </address>
</section>

<section class="card card--back" aria-label="Business card back">
  <svg class="card__shape" viewBox="0 0 560 320" preserveAspectRatio="none" aria-hidden="true">
    <path d="M120 320 C60 220 80 90 200 0 H230 C110 90 90 220 150 320 Z" fill="#ffffff" opacity=".05"/>
    <path d="M420 0 C500 90 520 220 470 320 H440 C490 220 470 90 390 0 Z" fill="#ffffff" opacity=".05"/>
  </svg>
  <div class="back-brand">
    <div class="back-brand__row">
      <span class="back-brand__dot"></span>
      <span class="back-brand__name">Tide Nook</span>
    </div>
    <p class="back-brand__tagline">Trailer boat syndication and management</p>
  </div>
</section>

</body>
</html>
```